Business Card Design Project

We need a business card to reflect the design of our website - just so it all ties in - it has a retro feel and can be found at http://www.velorasoulpair.com
We will need our phone 0437 215 964
Web address, and email velorapair@fernmail.com included
Our catch cry is "Classic Cocktail Music"
Perfect Live Music for Private & Corporate Events, Weddings and Dinner Music
Our names should be included :-
Maribel Thorne / piano & Dennis Holloway / bass
I am now also including our logo so that it can be included (in part or whole) somehow in the design
My partner thinks we should include our logo in some form in the design of the card - i will attach this here for you. I will attach eps but if you prefer another format please let me know
Regards
Mari

```html
<!DOCTYPE html>
<html lang="en">
<head>
<meta charset="utf-8">
<title>Velora Duo – Business Card</title>
<link href="https://fonts.googleapis.com/css2?family=Big+Shoulders+Display:wght@600&family=Josefin+Sans:wght@300;700&display=swap" rel="stylesheet">
<style>
  :root {
    --page: #ffffff;
    --teal: #7bb4b3;
    --cream: #ede3c9;
    --cream-shade: #b9ad97;
    --ink: #231f20;
    --badge: #5a5a58;
    --dot: #e6eeea;
    --white: #ffffff;
  }
  html, body {
    margin: 0; width: 1200px; height: 1000px; overflow: hidden;
    background: var(--page);
  }
  .card-art { display: block; }
  .deco {
    font-family: "Big Shoulders Display", sans-serif; font-weight: 600;
    text-transform: uppercase;
  }
  .member { fill: var(--ink); font-size: 42px; }
  .role { fill: var(--cream); font-size: 42px; }
  .badge-name { fill: var(--cream); font-size: 24px; letter-spacing: 2px; }
  .duo-name {
    font-family: "Josefin Sans", sans-serif; font-weight: 700; font-size: 112px;
    fill: var(--cream); filter: drop-shadow(4px 4px 3px rgba(0,0,0,0.45));
  }
  .tagline { fill: var(--ink); font-size: 58px; }
  .contact {
    font-family: "Josefin Sans", sans-serif; font-weight: 300; font-size: 25px;
    fill: var(--white);
  }
</style>
</head>
<body>
<svg class="card-art" width="1200" height="1000" viewBox="0 0 1200 1000" role="img" aria-label="Velora Duo business card">
  <defs>
    <pattern id="dot-row" width="20.7" height="8" patternUnits="userSpaceOnUse">
      <circle cx="4" cy="4" r="3" fill="var(--dot)"/>
    </pattern>
  </defs>

  <rect class="card" x="64" y="207" width="1049" height="599" fill="var(--teal)"/>

  <g class="dot-rules">
    <rect x="106" y="286" width="378" height="8" fill="url(#dot-row)"/>
    <rect x="106" y="353" width="378" height="8" fill="url(#dot-row)"/>
    <rect x="690" y="286" width="386" height="8" fill="url(#dot-row)"/>
    <rect x="690" y="353" width="386" height="8" fill="url(#dot-row)"/>
  </g>

  <g class="ribbon-tails">
    <polygon points="250,570 380,570 405,668 250,668 278,619" fill="var(--cream)"/>
    <polygon points="320,635 405,668 405,635" fill="var(--cream-shade)"/>
    <polygon points="895,570 765,570 740,668 895,668 867,619" fill="var(--cream)"/>
    <polygon points="826,635 740,668 740,635" fill="var(--cream-shade)"/>
  </g>
  <rect class="ribbon-band" x="320" y="540" width="506" height="95" fill="var(--cream)"/>

  <circle class="badge" cx="588" cy="321" r="69" fill="var(--badge)" stroke="var(--cream)" stroke-width="3"/>
  <text class="deco badge-name" x="588" y="330" text-anchor="middle">Velora</text>

  <text class="deco member" x="106" y="341" textLength="246" lengthAdjust="spacingAndGlyphs">Maribel Thorne</text>
  <text class="deco role" x="396" y="341" textLength="90" lengthAdjust="spacingAndGlyphs">Piano</text>
  <text class="deco member" x="691" y="341" textLength="246" lengthAdjust="spacingAndGlyphs">Dennis Holloway</text>
  <text class="deco role" x="1010" y="341" textLength="63" lengthAdjust="spacingAndGlyphs">Bass</text>

  <text class="duo-name" x="250" y="497" textLength="665" lengthAdjust="spacingAndGlyphs">VELORA DUO</text>

  <text class="deco tagline" x="337" y="607" textLength="466" lengthAdjust="spacingAndGlyphs">Classic Cocktail Music</text>

  <g class="contact" text-anchor="middle">
    <text x="562" y="713">tel: 0437 215 964</text>
    <text x="562" y="742">email: velorapair@fernmail.com</text>
    <text x="562" y="771">visit our site: www.velorasoulpair.com</text>
  </g>
</svg>
</body>
</html>
```